Business card design needed

I have started a new business called Marlow Auto Electrical, although the words Marlow Auto Electrical will be used on signage and documents I actually want to market the business as MAE. The services I offer are Mobile Auto Electrical, Automotive Air Conditioning and Test And Tag. My business will be targetting the Mining Industry, Civil, Rail, Agricultural and Workshop Testing And Tagging. My auto electrical service ranges from fault finding to new vehicle and mine compliance fit outs. I have a very strong focus on quality workmanship. I will upload the logo I have designed and want to use I am happy for the logo colour to change but the design itself must stay the same. I want the design to have a modern, eye catching, energetic feel. As I am a passionate motorsport fan I am happy for this to also influence the design. I am happy for the front of the card to have only the emblem and logo design and the back to have all the info.

Industry/Entity Type

Electrical

Contact Information for Business Card

MAE Marlow Auto Electrical, Dale Penrick, Auto Electrician, Mobile No 0417263859

Requirements
Must have
• On the business card it is mandatory that the following license numbers are shown:

MVRL38462
VDA L071348
ABN 61 839 204 518

```html
<!DOCTYPE html>
<html lang="en">
<head>
<meta charset="utf-8">
<title>Marlow Auto Electrical – Business Card</title>
<link rel="stylesheet" href="https://fonts.googleapis.com/css2?family=Saira+Semi+Condensed:wght@400;600&family=Arimo:wght@400&display=swap">
<style>
  :root {
    --ink: #111111;
    --paper: #ffffff;
    --accent: #fce51c;
    --muted: #555555;
    --rule: #444444;
  }
  html, body {
    margin: 0;
    padding: 0;
    width: 1200px;
    height: 741px;
    overflow: hidden;
    background: var(--paper);
  }
  .card {
    position: relative;
    width: 1200px;
    height: 741px;
    background: var(--paper);
    overflow: hidden;
  }
  .card__bands {
    position: absolute;
    inset: 0;
  }
  .brand {
    position: absolute;
    left: 117px;
    top: 205px;
    width: 420px;
    text-align: center;
    color: var(--ink);
    font-family: "Saira Semi Condensed", sans-serif;
    font-weight: 600;
  }
  .brand__mark {
    display: block;
    font-size: 200px;
    line-height: 180px;
    letter-spacing: 6px;
  }
  .brand__name {
    display: block;
    margin-top: 18px;
    font-size: 38px;
    line-height: 40px;
    text-transform: uppercase;
    letter-spacing: 0.5px;
  }
  .divider {
    position: absolute;
    left: 619px;
    top: 148px;
    width: 2px;
    height: 412px;
    background: var(--ink);
  }
  .contact {
    position: absolute;
    left: 703px;
    top: 240px;
    color: var(--ink);
  }
  .contact__name {
    margin: 0;
    font-family: "Saira Semi Condensed", sans-serif;
    font-weight: 400;
    font-size: 66px;
    line-height: 66px;
    text-transform: uppercase;
    letter-spacing: 0.5px;
  }
  .contact__role {
    margin: 0;
    font-family: "Arimo", sans-serif;
    font-size: 32px;
    line-height: 38px;
    color: var(--muted);
    padding-bottom: 8px;
    width: 322px;
    border-bottom: 2px solid var(--rule);
  }
  .contact__phone {
    margin: 8px 0 0;
    font-family: "Arimo", sans-serif;
    font-size: 26px;
    line-height: 32px;
  }
  .contact__licences {
    margin: 50px 0 0;
    padding: 0;
    list-style: none;
    font-family: "Arimo", sans-serif;
    font-size: 20px;
    line-height: 24px;
  }
</style>
</head>
<body>
  <main class="card">
    <svg class="card__bands" width="1200" height="741" viewBox="0 0 1200 741" aria-hidden="true">
      <polygon class="band band--top" points="0,0 1146,0 0,76" fill="var(--ink)"/>
      <polygon class="band band--bottom" points="0,741 1200,648 1200,741" fill="var(--accent)"/>
    </svg>

    <div class="brand">
      <span class="brand__mark">MAE</span>
      <span class="brand__name">Marlow Auto Electrical</span>
    </div>

    <div class="divider"></div>

    <section class="contact">
      <h1 class="contact__name">Dale Penrick</h1>
      <p class="contact__role">Auto Electrician</p>
      <p class="contact__phone">Mobile No.&nbsp; 0417263859</p>
      <ul class="contact__licences">
        <li>MVRL38462</li>
        <li>VDA L071348</li>
        <li>ABN 61 839 204 518</li>
      </ul>
    </section>
  </main>
</body>
</html>
```